Tradolo - Forex Signal Services Moments Matter Most. Shape your future.

I need an attractive eye catching web design that is azure friendly. I currently have a web programmer working on the backend of my website. Now I need a professional design to attract and retain customers. This site needs to be mobile friendly.

Tradolo is a highly reputable, trustworthy and professional site that offers forex signals to traders in all parts of the globe. With accurate and reliable forex signals, traders can not only make money but also boost their profits.

At Tradolo, we want our clients to have complete faith on us and our services! We also do not want our users to lead a simple and monotonous life. Instead our goal is to help them create an extra source of steady income. However, this is possible only when our clients resolve to change their lives for the better. They need to change their mindset and most importantly develop a positive frame of mind. That’s exactly why at Tradolo, we provide our clients with innumerable personal development tools and resources that’ll aid them in changing all the aspects of their lives. We want our traders to feel inspired and educate them in the right way!

Colors are flexible.

I do like the simplicity of www.brightmarkvo.example.
I do want a design more professional in appearance and not everything on page one.

I have not been able to decide on a logo. There is one of lower quality as I have not paid for it yet but I will if you decide it's the best for my business I will. Or should one feel that they have a better idea for a logo, I will pay for it if i like it.

I have included some of the content of my site so you can get a feel for where I am coming from.
(Please note that this content is still in the editing process)
Updates

Project Deadline Extended Reason: My content was not complete nor finalization of the final logo. We will allow a few more days for designers to modify the website.Thank you for your patience and understanding. Added Tuesday, January 24, 2017

Target Market(s)

I work with Forex Traders, Investors wanting to control their own portfolios, and remote nomads/mellienials

Coding

Number of Pages Required

Requirements
Must have
• I must have a professional clean look. I want the site to be interactive and eye catching. I want my audience hooked within seconds of opening it. It has to have all important information first. Photos must be legit and not spammy. I work as a representative in the financial market. I want my site to reflect that I stand by my product and reputation means everything to me. This site has to be engaging.
• Sorry, I should have included this earlier of what I will all need on this site.
• I'll have about Tradolo (my company, what we stand for, who we work with, my strategy, etc....
• about me (why i started this company, who I am)
• Performance (graphs and recent posts of signals)
• Membership (how to sign up)
• Terms of service/legal/disclaimers
• FAQS
• Personal Development Resources
• Forex Education Resources
Nice to have
• Quick links to bounce around the site faster.
Should not have
• I do not want over the top white collar conservative.

```html
<!DOCTYPE html>
<html lang="en">
<head>
<meta charset="utf-8">
<title>Tradolo – Forex Signal Services</title>
<link href="https://fonts.googleapis.com/css2?family=Open+Sans:wght@300;400;600;700&display=swap" rel="stylesheet">
<style>
:root{
  --orange:#ff7f1a;
  --orange-dark:#f26f0b;
  --ink:#222222;
  --text:#555555;
  --muted:#8a8a8a;
  --soft:#f7f7f7;
  --panel:#f4f4f4;
  --line:#d9d9d9;
  --white:#ffffff;
  --hero-a:#3b3f45;
  --hero-b:#15181c;
}
*{box-sizing:border-box;margin:0;padding:0}
html,body{width:1200px;height:3267px;overflow:hidden}
body{font-family:"Open Sans",Arial,sans-serif;color:var(--text);background:var(--white)}
.section-title{font-weight:400;color:var(--ink);text-align:center;font-size:29px;letter-spacing:.5px}
.btn{display:inline-block;background:var(--orange);color:var(--white);font-size:14px;font-weight:600;text-transform:uppercase;border-radius:5px;text-decoration:none;text-align:center}
.btn-outline{display:inline-block;border:1px solid var(--line);border-radius:5px;font-size:11px;color:var(--text);text-transform:uppercase;width:109px;height:42px;line-height:40px;text-align:center;background:var(--white)}

/* header */
.site-header{position:relative;height:98px;background:var(--white);box-shadow:0 1px 3px rgba(0,0,0,.06)}
.brand{position:absolute;left:172px;top:16px;display:flex;flex-direction:column;align-items:center;gap:4px}
.brand-dot{width:26px;height:26px;border-radius:50%;background:var(--orange)}
.brand-name{font-size:24px;font-weight:600;color:#4a4a4a;line-height:1}
.main-nav{position:absolute;top:40px;left:0;width:100%;font-size:12.5px;font-weight:600;color:var(--ink);text-transform:uppercase}
.main-nav span{position:absolute;white-space:nowrap}
.main-nav .active{color:var(--orange)}
.search-btn{position:absolute;left:1000px;top:32px;width:33px;height:33px;border-radius:50%;background:var(--orange);display:flex;align-items:center;justify-content:center}

/* hero */
.hero{position:relative;height:523px;overflow:hidden}
.hero-photo{position:absolute;inset:0;background:linear-gradient(110deg,var(--hero-a) 0%,#2a2e33 45%,var(--hero-b) 100%)}
.hero-copy{position:absolute;left:172px;top:273px;width:360px;color:var(--white);font-size:22px;line-height:30px;font-weight:400}
.hero .btn{position:absolute;left:172px;top:427px;width:209px;height:41px;line-height:41px}
.slider-dots{position:absolute;left:176px;top:540px;display:flex;gap:9px}
.slider-dots i{width:9px;height:9px;border-radius:50%;background:var(--white)}
.slider-dots i:first-child{background:var(--orange)}

/* welcome */
.welcome{height:377px;text-align:center;padding-top:60px}
.welcome .tagline{font-size:10px;text-transform:uppercase;color:var(--muted);margin-top:10px;letter-spacing:.3px}
.welcome p{width:910px;margin:42px auto 0;font-size:11px;line-height:23px;color:#444}
.welcome .btn{margin-top:46px;width:170px;height:40px;line-height:40px}

/* why us */
.why-us{height:490px;background:var(--soft);text-align:center;padding-top:78px}
.why-us p{width:910px;margin:0 auto;font-size:13px;line-height:25px;color:var(--muted)}
.why-us p:first-of-type{margin-top:48px}
.why-us p + p{margin-top:17px}
.why-us .btn{margin-top:42px;width:170px;height:42px;line-height:42px}

/* faq */
.faq{height:588px;background:var(--white);padding-top:60px}
.faq-panel{position:relative;margin:44px 0 0 144px;width:910px;height:390px;display:flex}
.faq-list{width:442px;list-style:none}
.faq-list li{position:relative;font-size:17px;color:var(--ink);padding-left:32px;line-height:25px}
.faq-list li::before{content:"";position:absolute;left:12px;top:9px;width:7px;height:7px;border-right:1.5px solid currentColor;border-bottom:1.5px solid currentColor;transform:rotate(-45deg)}
.faq-list li.active{background:var(--orange);color:var(--white);height:61px;line-height:61px;padding-left:34px}
.faq-list li.active::before{top:27px}
.faq-list li:nth-child(2){margin-top:38px}
.faq-list li:nth-child(3){margin-top:50px}
.faq-list li:nth-child(4){margin-top:48px}
.faq-answer{flex:1;background:var(--panel);padding:26px 30px 0 32px}
.faq-answer h3{font-size:19px;font-weight:600;color:var(--ink);margin-bottom:30px}
.faq-answer p{font-size:14.5px;line-height:26px;color:var(--muted)}
.faq-answer p + p{margin-top:20px}

/* offer */
.offer{height:582px;background:#f9f9f9;padding-top:80px}
.offer-grid{display:flex;gap:26px;margin:36px 0 0 144px}
.offer-card{width:286px}
.offer-card:last-child{width:287px}
.offer-photo{height:165px}
.photo-a{background:linear-gradient(135deg,#5a2c3a,#b4706a 55%,#2b2f44)}
.photo-b{background:linear-gradient(135deg,#8fa6c4,#3b5f8e 60%,#c7cfdc)}
.photo-c{background:linear-gradient(135deg,#d7dde3,#9aa8b4 55%,#eef1f3)}
.offer-card h3{margin-top:45px;font-size:14.5px;font-weight:600;color:var(--orange);text-transform:uppercase}
.offer-card p{margin-top:12px;font-size:11.5px;line-height:20px;color:#555;height:60px}
.offer-card .btn-outline{margin-top:20px}

/* steps */
.steps{height:239px;background:var(--white);padding-top:58px}
.step-row{position:relative;margin-top:48px;height:70px}
.step{position:absolute;top:0;display:flex;align-items:center;gap:8px}
.step b{font-size:30px;font-weight:600;color:var(--ink);line-height:1}
.step span{font-size:14px;line-height:17px;color:var(--ink)}

/* disclaimer */
.disclaimer{height:295px;background:var(--orange);color:var(--white);text-align:center;padding-top:48px}
.disclaimer h2{font-size:20px;font-weight:400;text-transform:uppercase}
.disclaimer p{width:820px;margin:14px auto 0;font-size:8.6px;line-height:17.5px}
.disclaimer p + p{margin-top:20px}

/* footer */
.site-footer{position:relative;height:75px;background:var(--white);font-size:11.5px;color:var(--ink)}
.footer-brand{position:absolute;left:172px;top:22px;display:flex;align-items:center;gap:8px}
.footer-brand .brand-dot{width:22px;height:22px}
.footer-brand .brand-name{font-size:22px}
.copyright{position:absolute;left:305px;top:30px;text-transform:uppercase}
.footer-links{position:absolute;left:802px;top:30px;text-transform:uppercase;word-spacing:2px}
</style>
</head>
<body>

<header class="site-header">
  <div class="brand"><span class="brand-dot"></span><span class="brand-name">Tradolo</span></div>
  <nav class="main-nav">
    <span class="active" style="left:431px">Home</span>
    <span style="left:497px">Why Us ?</span>
    <span style="left:577px">Forex Traders</span>
    <span style="left:688px">What We Do For You</span>
    <span style="left:849px">FAQ's</span>
    <span style="left:910px">Contact Us</span>
  </nav>
  <div class="search-btn">
    <svg width="14" height="14" viewBox="0 0 14 14"><circle cx="6" cy="6" r="4.3" fill="none" stroke="#fff" stroke-width="1.8"/><line x1="9.2" y1="9.2" x2="13" y2="13" stroke="#fff" stroke-width="1.8" stroke-linecap="round"/></svg>
  </div>
</header>

<section class="hero">
  <div class="hero-photo" role="img" aria-label="Businessman in a suit holding a tablet in front of a dark financial chart backdrop"></div>
  <p class="hero-copy">Tradolo is a highly reputable, trustworthy and professional site that offers forex signals to traders in all parts of the globe.</p>
  <a class="btn" href="#">Get Started Today</a>
  <div class="slider-dots"><i></i><i></i><i></i><i></i></div>
</section>

<section class="welcome">
  <h1 class="section-title">WELCOME TO TRADOLO.EXAMPLE!</h1>
  <div class="tagline">Forex signal services moments matter most, shape your future</div>
  <p>We use proven strategies to help traders in succeeding in the forex market. Our forex experts provide high-probability, professional and consistent forex signals and charts that help traders in maximizing their profits and eliminating losses. Try our free Currency Education service to find out what differentiates us from our competitors and how we can aid you in becoming a professional trader!</p>
  <a class="btn" href="#">Contact Us</a>
</section>

<section class="why-us">
  <h2 class="section-title">WHY US?</h2>
  <p>We're a small company based in the beautiful rockies, Pine Hollow, Alberta, Canada with over 9 years of successful trading experience in the foreign exchange market. We&nbsp; decided to launch our service for two reasons: learning to trade is a difficult process that leaves many aspiring traders frustrated, and on top of that, there is no shortage of bad signal services that take advantage of these traders.</p>
  <p>Our aim is to help aspiring traders become profitable while they're learning to trade, and even if they do not have the time or the skills to become profitable on their own, there is no reason why retail traders should not be allowed to take advantage of the forex market.</p>
  <a class="btn" href="#">Read More</a>
</section>

<section class="faq">
  <h2 class="section-title">FAQ'S</h2>
  <div class="faq-panel">
    <ul class="faq-list">
      <li class="active">What is your trading philosophy and style?</li>
      <li>How many signals do you send a month?</li>
      <li>How many pips can I make per month<br>following your signals?</li>
      <li>Can I follow your signals and have a full time job?</li>
    </ul>
    <div class="faq-answer">
      <h3>What is your trading philosophy and style?</h3>
      <p>We follow naked forex trading techniques including price action, immediate trend and&nbsp; personalized mathematical formulas.</p>
      <p>&nbsp;Our success stems from our strict enforcement of discipline, patience, attitude, economics and timing to help our traders maximize their gains from forex trading Obviously we do not always win, but our winning trades exceed those that are not and our take profit target is always bigger than our stop loss.</p>
    </div>
  </div>
</section>

<section class="offer">
  <h2 class="section-title">WHAT WE OFFER</h2>
  <div class="offer-grid">
    <article class="offer-card">
      <div class="offer-photo photo-a" role="img" aria-label="Close-up of a trading screen with glowing market charts"></div>
      <h3>Forex Traders</h3>
      <p>A Forex signal service is provided for those who are struggling to make money on the forex market.We know that the forex market is ruthless</p>
      <a class="btn-outline" href="#">Read More</a>
    </article>
    <article class="offer-card">
      <div class="offer-photo photo-b" role="img" aria-label="Hands typing on a laptop keyboard at a desk"></div>
      <h3>Investors and Retirees</h3>
      <p>If you are someone that has been tricked before or have lost your savings to investment companies and would like to know how you can take</p>
      <a class="btn-outline" href="#">Read More</a>
    </article>
    <article class="offer-card">
      <div class="offer-photo photo-c" role="img" aria-label="Laptop and coffee cup on a desk by a bright city window"></div>
      <h3>Work From Home</h3>
      <p>Work from home has become very popular over the years ever since the internet became available to more households around the world.</p>
      <a class="btn-outline" href="#">Read More</a>
    </article>
  </div>
</section>

<section class="steps">
  <h2 class="section-title">WHAT WE DO FOR YOU</h2>
  <div class="step-row">
    <div class="step" style="left:190px">
      <svg width="48" height="52" viewBox="0 0 48 52" fill="none" stroke="var(--orange)" stroke-width="2" stroke-linecap="round" stroke-linejoin="round"><path d="M16 30V8a4 4 0 0 1 8 0v16"/><path d="M24 22a4 4 0 0 1 8 0v4"/><path d="M32 24a4 4 0 0 1 8 0v8c0 10-6 16-14 16h-3c-5 0-8-3-11-7l-6-9a3.5 3.5 0 0 1 6-4l4 5"/><path d="M10 10a10 10 0 0 1 20 0"/></svg>
      <b>1</b><span>Choose the best<br>forex pair</span>
    </div>
    <div class="step" style="left:407px">
      <svg width="44" height="50" viewBox="0 0 44 50" fill="none" stroke="var(--orange)" stroke-width="2" stroke-linecap="round" stroke-linejoin="round"><path d="M6 28l10-10 8 8L38 10"/><path d="M30 10h8v8"/><path d="M6 48V38M16 48V32M26 48V36M36 48V26"/></svg>
      <b>2</b><span>Analyze the<br>forex chart</span>
    </div>
    <div class="step" style="left:634px">
      <svg width="60" height="44" viewBox="0 0 60 44" fill="none" stroke="var(--orange)" stroke-width="2" stroke-linecap="round" stroke-linejoin="round"><rect x="20" y="8" width="38" height="28" rx="2"/><path d="M20 10l19 14 19-14"/><path d="M2 14h12M6 22h8M2 30h12"/></svg>
      <b>3</b><span>Send Forex<br>Signals</span>
    </div>
    <div class="step" style="left:845px">
      <svg width="54" height="46" viewBox="0 0 54 46" fill="none" stroke="var(--orange)" stroke-width="2" stroke-linecap="round" stroke-linejoin="round"><path d="M10 20c0-8 8-14 20-14s20 6 20 14c0 6-3 10-7 12v8h-7v-5h-12v5h-7v-8c-3-2-5-4-6-6H5v-8h4"/><circle cx="38" cy="16" r="1.3" fill="var(--orange)"/><path d="M24 10h10"/></svg>
      <b>4</b><span>You&nbsp; make<br>Money</span>
    </div>
  </div>
</section>

<section class="disclaimer">
  <h2>Disclaimer</h2>
  <p>Disclaimer: Trading foreign exchange ("Forex") on margin carries a high level of risk, and may not be suitable for all investors. Before deciding to trade Forex you should carefully consider your investment objectives, level of experience, and appetite for risk. The possibility exists that you could sustain a loss in excess of your deposited funds and therefore you should not speculate with capital that you cannot afford to lose. You should be aware of all the risks associated with foreign exchange. Clients must be at least 18 years old to use the services of Tradolo. You acknowledge that past performance is not an indicator of future returns and that references to performance on this Site are provided as historical benchmarks only. Tradolo does not take responsibility for loss incurred as a result of our trading signals.</p>
  <p>By signing up as a member you acknowledge that we are not providing financial advice and<br>that you are making the decision to use our trades on your own account. All information provided by Tradolo in any form, is for educational purposes only.</p>
</section>

<footer class="site-footer">
  <div class="footer-brand"><span class="brand-dot"></span><span class="brand-name">Tradolo</span></div>
  <div class="copyright">© 2017 Company Name &nbsp;|&nbsp; All Rights Reserved</div>
  <div class="footer-links">Terms of Services &nbsp; | &nbsp; Privacy Policy &nbsp;| Help</div>
</footer>

</body>
</html>
```